Business Card For Quillmoor Financial Consulting

Hi, I would like a business card designed. Bold, modern.
Please use the same design as the logo. I have also attached the website design to see the overall theme.
Wordmark Font
Color: Hex: #01AEF7

```html
<!DOCTYPE html>
<html lang="en">
<head>
<meta charset="utf-8">
<title>Quillmoor Consulting – Business Card</title>
<link rel="stylesheet" href="https://fonts.googleapis.com/css2?family=Source+Sans+3:wght@400;600;700&display=swap">
<style>
  :root {
    --page-bg: #e4e5e6;
    --ink-dark: #13222b;
    --brand-blue: #2fa7de;
    --card-light: #f4f5f6;
    --text-dark: #1c2a33;
    --white: #ffffff;
    --watermark: #dfe9f1;
  }
  * { margin: 0; padding: 0; box-sizing: border-box; }
  html, body { width: 1200px; height: 960px; overflow: hidden; }
  body {
    background: var(--page-bg);
    font-family: "Source Sans 3", Arial, sans-serif;
    position: relative;
  }
  .card {
    position: absolute;
    left: 297px;
    width: 607px;
    height: 347px;
    overflow: hidden;
  }

  /* Front */
  .card-front { top: 110px; background: var(--ink-dark); }
  .front-texture {
    position: absolute; inset: 0;
    background:
      radial-gradient(ellipse 70% 90% at 0% 0%, rgba(200,215,225,0.28), rgba(200,215,225,0) 70%),
      linear-gradient(90deg, rgba(255,255,255,0.05), rgba(0,0,0,0.15));
  }
  .front-brand {
    position: absolute;
    left: 146px; top: 148px;
    display: flex; align-items: center; gap: 12px;
  }
  .brand-square {
    width: 50px; height: 50px;
    border: 4px solid var(--brand-blue);
  }
  .brand-name {
    font-weight: 700;
    color: var(--white);
    line-height: 1;
    text-transform: uppercase;
  }
  .front-brand .brand-name { font-size: 40px; letter-spacing: 1px; }
  .brand-name .sub {
    display: block;
    font-size: 12px;
    letter-spacing: 9.6px;
    margin-top: 6px;
  }

  /* Back */
  .card-back { top: 510px; background: var(--card-light); }
  .back-band {
    position: absolute; left: 0; top: 0;
    width: 59px; height: 100%;
    background: var(--ink-dark);
  }
  .back-decoration {
    position: absolute;
    left: 288px; top: 20px;
    width: 300px; height: 327px;
    background: linear-gradient(200deg, var(--watermark) 0%, rgba(223,233,241,0.6) 60%, rgba(223,233,241,0) 100%);
  }
  .back-brand {
    position: absolute;
    left: 33px; top: 38px;
    display: flex; align-items: center; gap: 9px;
  }
  .back-brand .brand-square { width: 46px; height: 46px; border-width: 3px; }
  .back-brand .brand-name { color: var(--text-dark); font-size: 34px; letter-spacing: 1px; }
  .back-brand .brand-name .sub { font-size: 11px; letter-spacing: 8.4px; margin-top: 5px; }

  .person { position: absolute; left: 88px; top: 126px; }
  .person-name { color: var(--brand-blue); font-weight: 600; font-size: 20px; line-height: 24px; }
  .person-title { color: var(--text-dark); font-size: 16px; line-height: 20px; }
  .divider {
    position: absolute; left: 88px; top: 183px;
    width: 33px; height: 2px; background: var(--brand-blue);
  }
  .contacts {
    position: absolute; left: 88px; top: 200px;
    list-style: none;
    color: var(--text-dark);
    font-size: 15.5px; line-height: 21px;
  }
  .contacts li { display: flex; align-items: flex-start; gap: 6px; }
  .contacts li.gap { margin-top: 7px; }
  .contacts svg {
    width: 13px; height: 13px; flex: none; margin-top: 4px;
    fill: none; stroke: var(--brand-blue); stroke-width: 1.6;
  }
</style>
</head>
<body>
  <section class="card card-front">
    <div class="front-texture" role="img" aria-label="Repeating grid of brand emblems fading from silver to dark"></div>
    <div class="front-brand">
      <span class="brand-square"></span>
      <p class="brand-name">Quillmoor<span class="sub">Consulting</span></p>
    </div>
  </section>

  <section class="card card-back">
    <div class="back-band"></div>
    <div class="back-decoration" role="img" aria-label="Large faint brand emblem in the background"></div>
    <div class="back-brand">
      <span class="brand-square"></span>
      <p class="brand-name">Quillmoor<span class="sub">Consulting</span></p>
    </div>
    <div class="person">
      <p class="person-name">Daniel Harper</p>
      <p class="person-title">President</p>
    </div>
    <div class="divider"></div>
    <ul class="contacts">
      <li>
        <svg viewBox="0 0 14 14"><path d="M7 13s-4.5-4.6-4.5-7.6a4.5 4.5 0 0 1 9 0C11.5 8.4 7 13 7 13z"/><circle cx="7" cy="5.5" r="1.6"/></svg>
        <span>418 Alder Crest Way, Suite 210<br>Fairbrook, CA 95012</span>
      </li>
      <li class="gap">
        <svg viewBox="0 0 14 14"><path d="M3 1.5l2.2 2.8-1.2 1.6c.8 1.7 2.2 3.1 3.9 3.9l1.6-1.2 2.8 2.2-1.3 1.7C6.5 12.4 1.6 7.5 1.3 2.8z"/></svg>
        <span>555-014-2378</span>
      </li>
      <li>
        <svg viewBox="0 0 14 14"><rect x="1.2" y="2.8" width="11.6" height="8.4"/><path d="M1.2 3l5.8 4.6L12.8 3"/></svg>
        <span>daniel@quillmoor.com</span>
      </li>
      <li>
        <svg viewBox="0 0 14 14"><circle cx="7" cy="7" r="5.8"/><ellipse cx="7" cy="7" rx="2.5" ry="5.8"/><path d="M1.2 7h11.6"/></svg>
        <span>www.quillmoor.com</span>
      </li>
    </ul>
  </section>
</body>
</html>
```